Website Header Development

I am after a redesign of the Header of a website www.qlvoltrix.com.au.
This project is for the header only, and should fit in with the rest of the site
Target Market(s)
Business
Requirements
Should not have
- Over the top. Keep it simple

```html
<!DOCTYPE html>
<html lang="en">
<head>
<meta charset="utf-8">
<title>Qlvoltrix Energy – Resource Efficiency</title>
<link rel="stylesheet" href="https://fonts.googleapis.com/css2?family=Alegreya+Sans:wght@400;500;700&family=Crete+Round&display=swap">
<style>
:root{
  --page-bg:#f1f1f1;
  --panel:#ffffff;
  --nav-green:#2e8b3e;
  --nav-dark:#167a3a;
  --nav-text:#ffffff;
  --logo-blue:#1d3a8a;
  --title-navy:#0c0c6e;
  --side-heading:#27388a;
  --text-dark:#1b1b1b;
  --text-grey:#6a6a6a;
  --field-border:#b9b9b9;
  --sky-top:#8fc2ea;
  --sky-mid:#dcecf8;
  --grass:#7cc13a;
}
*{box-sizing:border-box;margin:0;padding:0}
html,body{width:1200px;height:1085px;overflow:hidden}
body{background:var(--page-bg);font-family:"Alegreya Sans",sans-serif;color:var(--text-dark);position:relative}
.site{position:absolute;left:19px;top:0;width:1161px;height:1085px;background:var(--panel);overflow:hidden}
.masthead{position:absolute;left:0;top:0;width:1161px;height:137px;
  background:linear-gradient(180deg,var(--sky-top) 0%,var(--sky-mid) 62%,var(--grass) 88%,#4f9a25 100%)}
.brand{position:absolute;left:21px;top:56px;display:flex;align-items:center;gap:10px;
  font-family:"Alegreya Sans",sans-serif;font-weight:700;font-size:40px;color:var(--logo-blue);letter-spacing:-.5px}
.brand-mark{width:22px;height:22px;background:var(--logo-blue);border-radius:50%}
.nav{position:absolute;left:0;top:137px;width:1161px;height:62px;background:var(--nav-green);overflow:hidden}
.nav-shade{position:absolute;right:0;top:0}
.nav a{position:absolute;top:0;line-height:56px;color:var(--nav-text);text-decoration:none;font-size:14px;font-weight:500}
.nav a.major{font-size:17px;font-weight:700;line-height:62px}
.main{position:absolute;left:0;top:199px;width:840px;height:886px}
.page-title{position:absolute;left:0;top:36px;width:860px;text-align:center;
  font-family:"Crete Round",serif;font-weight:400;font-size:28px;color:var(--title-navy)}
.copy{position:absolute;left:68px;font-size:17px;line-height:29px;color:var(--text-dark)}
.copy.muted{color:var(--text-grey)}
.copy ul{list-style:none}
.copy li{position:relative;padding-left:26px}
.copy li::before{content:"";position:absolute;left:8px;top:12px;width:6px;height:6px;background:var(--text-grey)}
.feature-photo{position:absolute;left:334px;top:106px;width:407px;height:271px;
  background:linear-gradient(135deg,#e9ecef 0%,#cfd6dc 45%,#b7c9d6 70%,#eef1f3 100%)}
.sidebar{position:absolute;left:855px;top:199px;width:300px;height:886px}
.search{position:absolute;left:0;top:1px;width:213px;height:36px;border:1px solid #d3d3d3;
  display:flex;align-items:center;gap:8px;padding-left:10px;font-size:15px;color:#9a9a9a;font-family:Arial,sans-serif}
.widget-title{position:absolute;left:0;top:80px;font-family:"Crete Round",serif;font-size:24px;line-height:35px;
  letter-spacing:2px;color:var(--side-heading)}
.widget-note{position:absolute;left:0;font-size:12.5px;line-height:29px;font-weight:700;color:var(--text-dark)}
.field{position:absolute;left:0;width:204px;height:34px;border:1px solid var(--field-border);background:#fff}
.field.area{width:225px;height:200px}
</style>
</head>
<body>
<div class="site">
  <header class="masthead" role="img" aria-label="Header photo: blue sky with clouds, green grass along the bottom and a coin dropping into a white piggy bank at the right">
    <div class="brand"><span>qlvoltrix energy</span><span class="brand-mark"></span></div>
  </header>

  <nav class="nav">
    <svg class="nav-shade" width="120" height="62" viewBox="0 0 120 62"><polygon points="0,0 120,0 120,62 62,62" fill="var(--nav-dark)"/></svg>
    <a class="major" style="left:98px">Home</a>
    <a style="left:184px">About Us</a>
    <a style="left:276px">Services</a>
    <a style="left:360px">Projects and Case Studies</a>
    <a class="major" style="left:548px">Financial Information</a>
    <a style="left:754px">News</a>
    <a style="left:822px">Contact</a>
  </nav>

  <main class="main">
    <h1 class="page-title">Resource Efficiency – Sustainable Solutions</h1>
    <div class="feature-photo" role="img" aria-label="Photo: a businessman holding a blue jigsaw piece beside puzzle outlines and the word Solution"></div>

    <p class="copy" style="top:92px">Is your business performing as<br>well as your competitors?</p>
    <p class="copy" style="top:181px">Are your fixed costs<br>comparable to industry<br>leaders?</p>
    <p class="copy" style="top:298px">Is your business becoming less<br>profitable with increased<br>energy, waste and water prices?</p>
    <p class="copy" style="top:415px">Do you wish to reduce your impact on the environment through reducing the use of resources<br>(energy, waste and water) within your business?</p>
    <p class="copy muted" style="top:504px">If so, Qlvoltrix can assist your business to achieve its core functions in the most effective<br>manner.</p>
    <p class="copy muted" style="top:592px">Qlvoltrix can assist your business in achieving improved productivity through the<br>implementation of:</p>
    <div class="copy muted" style="top:680px;left:96px">
      <ul>
        <li>innovative and targeted resource efficiency strategies</li>
        <li>streamlined business strategies</li>
      </ul>
    </div>
    <p class="copy muted" style="top:769px">Join other businesses across Australia in improving resource efficiency and achieving a<br>competitive advantage for your business.</p>
    <p class="copy" style="top:857px">Can you afford not to take charge? Do you wish to identify a pathway to improving your</p>
  </main>

  <aside class="sidebar">
    <div class="search">
      <svg width="15" height="15" viewBox="0 0 15 15"><circle cx="6" cy="6" r="4.5" fill="none" stroke="#9a9a9a" stroke-width="2"/><line x1="9.5" y1="9.5" x2="14" y2="14" stroke="#9a9a9a" stroke-width="2"/></svg>
      <span>Search</span>
    </div>
    <h2 class="widget-title">Qlvoltrix<br>Energy<br>Newsletter</h2>
    <p class="widget-note" style="top:203px;width:215px">Would you like to receive our regular monthly Newsletter? Please fill in your Name:</p>
    <div class="field" style="top:302px"></div>
    <p class="widget-note" style="top:349px;width:225px">Let us know your email address so we can send the Newsletter directly to your email address. (Note that your details will not be passed onto any 3rd parties. Your details stricly remain with Qlvoltrix Energy for the purposes of sending you the Qlvoltrix Energy Newsletter)</p>
    <div class="field" style="top:592px"></div>
    <p class="widget-note" style="top:639px;width:225px">Further, please let us know if there are particular topics you would like to hear about in our Newsletters</p>
    <div class="field area" style="top:737px"></div>
  </aside>
</div>
</body>
</html>
```